Lantern Advisory Website

I currently have a website www.lanternadvisoryinc.example. We are a IT Consulting Company. Our website will pretty much tell out our services. I am looking to enhance my website and make it look more professional. Looking for very classy and Contemporary look and design for my website.

It Company

```html
<!DOCTYPE html>
<html lang="en">
<head>
<meta charset="utf-8">
<title>Lantern Advisory</title>
<link href="https://fonts.googleapis.com/css2?family=Titillium+Web:wght@400;600;700&family=Roboto:wght@400;500;700&display=swap" rel="stylesheet">
<style>
:root{
  --blue:#12a3e0;
  --dark:#2b3035;
  --darker:#222528;
  --cta:#333537;
  --ink:#222;
  --muted:#666;
  --soft:#f2f2f2;
  --line:#d9d9d9;
  --white:#fff;
}
*{margin:0;padding:0;box-sizing:border-box}
html,body{width:718px;height:1200px;overflow:hidden}
body{position:relative;background:var(--white);font-family:Roboto,Arial,sans-serif;color:var(--ink)}
.abs{position:absolute}
/* header */
.header{position:absolute;left:0;top:0;width:718px;height:67px;background:var(--white)}
.topbar{position:absolute;left:224px;top:0;right:0;height:24px;background:var(--dark);display:flex;justify-content:flex-end;align-items:center;gap:18px;padding-right:30px;font-size:7px;color:#cfd4d8}
.topbar span{display:flex;align-items:center;gap:5px}
.logo-panel{position:absolute;left:0;top:0;width:240px;height:67px;background:#eef1f3;clip-path:polygon(0 0,224px 0,240px 67px,0 67px)}
.logo{position:absolute;left:96px;top:20px;display:flex;align-items:center;gap:7px}
.logo i{width:18px;height:18px;background:var(--blue);display:block}
.logo b{font-family:'Titillium Web',sans-serif;font-weight:700;font-size:15px;color:#1d4f9c;letter-spacing:.3px}
.nav{position:absolute;left:275px;top:38px;display:flex;gap:0;font-size:7px;font-weight:500}
.nav a{color:#333;text-decoration:none;padding:4px 10px;height:15px}
.nav a.active{background:var(--blue);color:var(--white)}
/* hero */
.hero{position:absolute;left:0;top:67px;width:718px;height:216px;background:linear-gradient(135deg,#3c4248,#2a2e33 45%,#4a4e52);}
.hero-shade{position:absolute;inset:0;background:rgba(20,24,28,.35)}
.hero h1{position:absolute;left:0;width:718px;top:40px;text-align:center;font-family:'Titillium Web',sans-serif;font-weight:600;font-size:22px;color:var(--white)}
.hero h1 em{font-style:normal;color:var(--blue)}
.hero h2{position:absolute;left:0;width:718px;top:65px;text-align:center;font-family:'Titillium Web',sans-serif;font-weight:400;font-size:14px;color:var(--white)}
.hero p{position:absolute;left:0;width:718px;top:94px;text-align:center;font-family:'Titillium Web',sans-serif;font-size:9px;line-height:12px;color:var(--white)}
.btn-more{position:absolute;left:305px;top:139px;width:90px;height:24px;display:flex;font-size:7px;font-weight:700}
.btn-more span{background:var(--blue);color:var(--white);width:62px;display:flex;align-items:center;padding-left:9px;clip-path:polygon(0 0,100% 0,88% 100%,0 100%)}
.btn-more b{flex:1;background:#e9eef1;display:flex;align-items:center;justify-content:center;margin-left:-8px;color:#333}
.arrow-l,.arrow-r{position:absolute;top:142px;width:10px;height:19px;border:1px solid #ddd;display:flex;align-items:center;justify-content:center}
.arrow-l{left:24px}
.arrow-r{left:684px;background:var(--blue);border-color:var(--blue)}
/* section heading */
.sec-title{position:absolute;left:93px;height:22px;background:var(--dark);color:var(--white);font-family:'Titillium Web',sans-serif;font-weight:700;font-size:11px;letter-spacing:.4px;display:flex;align-items:center;padding:0 22px 0 7px;clip-path:polygon(0 0,92% 0,100% 100%,0 100%)}
.sec-title em{font-style:normal;color:var(--blue);margin-left:3px}
.intro{position:absolute;left:93px;width:530px;font-size:7px;line-height:9px;color:var(--muted)}
/* welcome */
.welcome{position:absolute;left:0;top:283px;width:718px;height:289px;background:var(--soft)}
.card{position:absolute;top:91px;width:158px;height:175px;background:var(--white)}
.card .img{height:100px;clip-path:polygon(0 0,100% 0,100% 78%,0 100%)}
.card h3{position:absolute;left:18px;top:106px;font-size:8px;font-weight:500;letter-spacing:.3px;border-left:3px solid var(--blue);padding-left:5px;line-height:9px}
.card p{position:absolute;left:18px;top:127px;width:130px;font-size:6.5px;line-height:8.5px;color:var(--muted)}
.card a{position:absolute;left:18px;top:158px;font-size:6.5px;color:#333;text-decoration:none}
.card a.hot{color:var(--blue)}
/* services */
.tabs{position:absolute;left:93px;top:654px;width:530px;height:29px;display:flex;border:1px solid var(--line)}
.tab{flex:1;display:flex;align-items:center;gap:7px;padding-left:12px;font-size:7px;font-weight:500;border-left:1px solid var(--line);color:#333}
.tab:first-child{border-left:0;background:var(--blue);color:var(--white)}
.svc-h{position:absolute;left:93px;font-size:8.5px;font-weight:500}
.svc-p{position:absolute;left:93px;width:255px;font-size:7px;line-height:9px;color:var(--muted)}
.tech-list{position:absolute;left:93px;top:793px;list-style:none}
.tech-list li{display:flex;align-items:center;gap:7px;height:20.5px;font-size:7px;color:#333}
.tech-list b{width:14px;height:14px;border:1px solid var(--blue);border-radius:50%;display:flex;align-items:center;justify-content:center;font-size:6.5px;font-weight:500}
/* news */
.news{position:absolute;left:0;top:872px;width:718px;height:210px;background:var(--soft)}
.news-nav{position:absolute;top:28px;width:11px;height:19px;border:1px solid #ccc;background:var(--white);display:flex;align-items:center;justify-content:center}
.news-card{position:absolute;top:61px;width:258px;height:120px;background:var(--white);border:1px solid #e6e6e6}
.news-card .img{position:absolute;left:0;top:0;width:121px;height:118px}
.news-card h4{position:absolute;left:135px;top:20px;width:110px;font-size:8px;font-weight:500;line-height:10.5px}
.news-card .meta{position:absolute;left:135px;top:46px;font-size:6px;color:#999}
.news-card p{position:absolute;left:135px;top:62px;width:115px;font-size:6.5px;line-height:8.5px;color:var(--muted)}
.news-card a{position:absolute;left:135px;top:96px;font-size:6.5px;color:#333;text-decoration:none}
.news-card a.hot{color:var(--blue)}
/* cta */
.cta{position:absolute;left:0;top:1082px;width:718px;height:80px;background:var(--cta)}
.cta h3{position:absolute;left:93px;top:22px;font-family:'Titillium Web',sans-serif;font-weight:400;font-size:14.5px;color:var(--blue)}
.cta p{position:absolute;left:93px;top:42px;width:350px;font-size:7px;line-height:9px;color:#cfcfcf}
.cta-btn{position:absolute;left:534px;top:30px;width:91px;height:24px;display:flex;font-size:7px;font-weight:700}
.cta-btn span{background:var(--blue);color:var(--white);width:66px;display:flex;align-items:center;justify-content:center;clip-path:polygon(0 0,100% 0,88% 100%,0 100%)}
.cta-btn b{flex:1;background:var(--white);margin-left:-8px;display:flex;align-items:center;justify-content:center}
/* footer */
.footer{position:absolute;left:0;top:1162px;width:718px;height:38px;background:var(--darker)}
.social{position:absolute;left:93px;top:13px;display:flex;gap:4px}
.social i{width:12px;height:12px;border-radius:50%;background:#bfbfbf;display:block}
.social i.on{background:var(--blue)}
.foot-links{position:absolute;right:93px;top:12px;font-size:6px;font-style:italic;color:#aaa;letter-spacing:.2px}
.foot-links .on{color:var(--blue)}
.copy{position:absolute;right:93px;top:23px;font-size:5.5px;color:#aaa;letter-spacing:.2px}
</style>
</head>
<body>

<header class="header">
  <div class="logo-panel"></div>
  <div class="logo"><i></i><b>LANTERN ADVISORY</b></div>
  <div class="topbar">
    <span><svg width="12" height="8" viewBox="0 0 12 8"><rect x="0.5" y="0.5" width="11" height="7" fill="none" stroke="#12a3e0"/><path d="M0.5 0.5 6 4.5 11.5 0.5" fill="none" stroke="#12a3e0"/></svg>info@lanternadvisoryinc.example</span>
    <span><svg width="8" height="8" viewBox="0 0 8 8"><path d="M1 1.5c0 3 2.5 5.5 5.5 5.5l.8-1.5-1.8-1-.8.8C3.7 4.8 3.2 4.3 2.7 3.3l.8-.8-1-1.8z" fill="none" stroke="#12a3e0" stroke-width=".9"/></svg>+1 (555) 014 2290</span>
  </div>
  <nav class="nav">
    <a class="active">HOME</a><a>ABOUT US</a><a>SERVICES</a><a>SOLUTIONS</a><a>RESOURCES</a><a>CAREER</a><a>CONTACT US</a>
  </nav>
</header>

<section class="hero" role="img" aria-label="Desk seen from above with laptop, tablet, pencils and hand-drawn charts">
  <div class="hero-shade"></div>
  <h1><em>Lantern Advisory</em> Global Services</h1>
  <h2>Digital Specialists for the Glazing Industry</h2>
  <p>Our expert IT consultants and trainers use proven methodologies<br>to help you optimize costs, reduce risk, and see a faster return on your IT investments.</p>
  <div class="btn-more"><span>Learn More</span><b>→</b></div>
  <div class="arrow-l"><svg width="5" height="8" viewBox="0 0 5 8"><path d="M4 .5 1 4l3 3.5" fill="none" stroke="#ddd"/></svg></div>
  <div class="arrow-r"><svg width="5" height="8" viewBox="0 0 5 8"><path d="M1 .5 4 4 1 7.5" fill="none" stroke="#fff"/></svg></div>
</section>

<section class="welcome">
  <div class="sec-title" style="top:23px">WELCOME TO <em>LANTERN ADVISORY</em></div>
  <p class="intro" style="top:63px">Today's IT market is a dynamic, fast-paced industry, with ever-increasing demands. Meeting these demands for over 25 years, Lantern Advisory maintains a global presence, aggressively recruiting expertly qualified IT and Management Professionals from around.</p>
  <div class="card" style="left:93px">
    <div class="img" role="img" aria-label="Business people shaking hands in an office" style="background:linear-gradient(135deg,#dfe6ee,#8c9bab)"></div>
    <h3>CONSULTING</h3>
    <p>Lantern Advisory has certified professional consultants to work with...</p>
    <a>READ MORE</a>
  </div>
  <div class="card" style="left:280px">
    <div class="img" role="img" aria-label="Hand touching a glowing network diagram" style="background:linear-gradient(135deg,#1b1d20,#4a4e53)"></div>
    <h3>STAFF AUGMENTATION</h3>
    <p>For years Lantern Advisory has been offering our customers the ability to augment...</p>
    <a class="hot">READ MORE</a>
  </div>
  <div class="card" style="left:466px">
    <div class="img" role="img" aria-label="Offshore oil platform at sunset" style="background:linear-gradient(180deg,#7d8fa0,#2e3a48 70%,#b4683a)"></div>
    <h3>OFFSHORE</h3>
    <p>Our Offshore development model has a unique...</p>
    <a>READ MORE</a>
  </div>
</section>

<section class="services">
  <div class="sec-title" style="top:598px">OUR <em>SERVICES</em></div>
  <p class="intro" style="top:627px">Lantern Advisory Training programs are perfect for individuals to enhance their careers. Our hands-on practical and interactive programs use real time environment and equipment while our emphasis on real world job skills, problem solving, and other relevant training.</p>
  <div class="tabs">
    <div class="tab"><svg width="16" height="13" viewBox="0 0 16 13"><rect x="2" y="3" width="12" height="8" fill="none" stroke="#fff"/><path d="M1 12h14M5 3V1M11 3V1" stroke="#fff"/></svg>Technology</div>
    <div class="tab"><svg width="16" height="13" viewBox="0 0 16 13"><rect x="1" y="1" width="14" height="9" fill="none" stroke="#12a3e0"/><path d="M5 12h6M3 8l3-3 2 2 4-4" fill="none" stroke="#12a3e0"/></svg>Business</div>
    <div class="tab"><svg width="10" height="14" viewBox="0 0 10 14"><rect x="1" y="1" width="8" height="12" rx="1.5" fill="none" stroke="#12a3e0"/><circle cx="5" cy="10.5" r=".8" fill="#12a3e0"/></svg>App Development</div>
    <div class="tab"><svg width="14" height="14" viewBox="0 0 14 14"><rect x="3" y="3" width="8" height="8" fill="none" stroke="#12a3e0"/><path d="M5 1v2M9 1v2M5 11v2M9 11v2M1 5h2M1 9h2M11 5h2M11 9h2" stroke="#12a3e0"/></svg>Enterprise Overview</div>
    <div class="tab"><svg width="16" height="12" viewBox="0 0 16 12"><path d="M1 5l4-3 3 2 3-2 4 3-5 5-2-2-2 2z" fill="none" stroke="#12a3e0"/></svg>IT Consulting</div>
  </div>
  <div class="svc-h" style="top:700px">Technology</div>
  <p class="svc-p" style="top:714px">We are successful in deploying all students we trained into project with 2-3 weeks after training program. Our training programs will last for 6-8 weeks dependents on technology.</p>
  <p class="svc-p" style="top:751px">We will provide on job support for trainees until technology comfort level is attained.</p>
  <div class="svc-h" style="top:777px">Technologies</div>
  <ul class="tech-list">
    <li><b>1</b>TRAINING</li>
    <li><b>2</b>TECHNOLOGY REFRESH</li>
    <li><b>3</b>CAPACITY ON DEMAND</li>
  </ul>
  <div class="abs" role="img" aria-label="Hands holding a globe connected to laptop, tablet and phone" style="left:369px;top:702px;width:254px;height:147px;border:1px solid #ccc;background:linear-gradient(135deg,#3b4654,#8799ad 55%,#c8d3de)"></div>
</section>

<section class="news">
  <div class="sec-title" style="top:26px">LATEST <em>NEWS</em></div>
  <div class="news-nav" style="left:599px;background:var(--blue);border-color:var(--blue)"><svg width="5" height="8" viewBox="0 0 5 8"><path d="M4 .5 1 4l3 3.5" fill="none" stroke="#fff"/></svg></div>
  <div class="news-nav" style="left:614px"><svg width="5" height="8" viewBox="0 0 5 8"><path d="M1 .5 4 4 1 7.5" fill="none" stroke="#555"/></svg></div>
  <div class="news-card" style="left:94px">
    <div class="img" role="img" aria-label="Glowing digital globe above an open hand" style="background:radial-gradient(circle at 55% 40%,#6cc6f5,#123a6b 55%,#0a1a33)"></div>
    <h4>Lorem Ipsum simply dummy Text</h4>
    <div class="meta">By Admin at mar 03, 2016</div>
    <p>Quisque ut nisl et neque blandit quis interdum loremmassaut nisl et neque blandit ...</p>
    <a>Learn More →</a>
  </div>
  <div class="news-card" style="left:366px">
    <div class="img" role="img" aria-label="Offshore vessel with crane on the sea" style="background:linear-gradient(180deg,#5b7088,#a7b3bd 50%,#3b4a5a)"></div>
    <h4>Lorem Ipsum simply dummy Text</h4>
    <div class="meta">By Admin at mar 03, 2016</div>
    <p>Quisque ut nisl et neque blandit quis interdum loremmassaut nisl et neque blandit ...</p>
    <a class="hot">Learn More →</a>
  </div>
</section>

<section class="cta">
  <h3>Get Started Today for a Free Home Evaluation</h3>
  <p>Lorem Ipsum is simply dummy text of the printing and typesetting industry. Lorem Ipsum has been the industry's standard dummy text ever</p>
  <div class="cta-btn"><span>Contact Us</span><b><svg width="16" height="10" viewBox="0 0 16 10"><rect x="4" y="1" width="11" height="8" fill="none" stroke="#333"/><path d="M4 1l5.5 4L15 1M0 4h3M1 6h2" fill="none" stroke="#333"/></svg></b></div>
</section>

<footer class="footer">
  <div class="social"><i></i><i class="on"></i><i></i><i></i><i></i></div>
  <div class="foot-links">HOME &nbsp;/&nbsp; ABOUT US &nbsp;/&nbsp; COMPANY &nbsp;/&nbsp; <span class="on">SERVICES</span> &nbsp;/&nbsp; SOLUTIONS &nbsp;/&nbsp; RESOURCES &nbsp;/&nbsp; CAREER &nbsp;/&nbsp; CONTACT US</div>
  <div class="copy">COPYRIGHT @ LANTERN ADVISORY 2016,</div>
</footer>

</body>
</html>
```